Erstellung eines Polizeiwimpels für Kinder
Zielgruppe
Wir stellen Fahrradwimpel für Kinder her. Hier finden Sie unsere Produkte: https://www.kramladen.de/stores/node/58203916472
Aufgabenstellung
Wir möchten einen 'Polizeiwimpel' für Kinder herstellen.
Wenn möglich, nur eine Farbe verwenden (reduziert Kosten in der Produktion). Der Hintergrund soll 'Polizei Blau' sein.
Wimpelgröße: 17,5 cm X 32 cm X 32cm (Dreieckig)
Ich habe ein selbst erstelltes Design hochgeladen. Es soll den Schriftzug 'Polizei' enthalten und evtl. noch 'Polizei Symbole', die Jungs (und ihre Eltern) ansprechen. (Pistole, Sheriffstern, etc.) Das offizielle Wappen oder andere Hoheitssymbole dürfen wir allerdings nicht verwenden.

```html
<!DOCTYPE html>
<html lang="de">
<head>
<meta charset="utf-8">
<title>Polizeiwimpel</title>
<link rel="stylesheet" href="https://fonts.googleapis.com/css2?family=Arimo:wght@400;700&display=swap">
<style>
  :root {
    --police-blue: #25356f;
    --police-blue-light: #3b4b86;
    --ink-white: #ffffff;
    --page: #ffffff;
  }
  html, body {
    margin: 0;
    padding: 0;
    width: 1200px;
    height: 728px;
    overflow: hidden;
    background: var(--page);
  }
  .pennant {
    display: block;
    width: 1200px;
    height: 728px;
  }
  .pennant-body { fill: var(--police-blue); }
  .seam {
    fill: none;
    stroke: var(--ink-white);
    stroke-width: 6;
    stroke-dasharray: 40 20;
  }
  .artwork-slot { fill: var(--police-blue-light); }
  .wordmark {
    font-family: "Arimo", Arial, sans-serif;
    font-weight: 700;
    font-size: 156px;
    fill: var(--ink-white);
  }
  .web-address {
    font-family: "Arimo", Arial, sans-serif;
    font-weight: 400;
    font-size: 20px;
    fill: var(--ink-white);
  }
</style>
</head>
<body>
<svg class="pennant" viewBox="0 0 1200 728" xmlns="http://www.w3.org/2000/svg">
  <polygon class="pennant-body" points="40,56 1136,360 40,656"/>

  <line class="seam" x1="96" y1="86" x2="956" y2="322"/>
  <line class="seam" x1="96" y1="606" x2="956" y2="396"/>

  <rect class="artwork-slot" x="74" y="256" width="160" height="184" rx="10"
        role="img" aria-label="Platz für ein Polizei-Symbol, weiß auf Blau"/>

  <circle class="artwork-slot" cx="990" cy="358" r="20"
          role="img" aria-label="Platz für ein kleines Schmuckzeichen an der Wimpelspitze"/>

  <text class="wordmark" x="252" y="410">Polizei</text>

  <text class="web-address" x="92" y="588" transform="rotate(-14 92 588)">www.radwimpel.bike</text>
</svg>
</body>
</html>
```